Business Card Design

We have our logo and everything in place. Looking to have a layout for our new business cards designed. These will be printed with a matte finish, possibly rounded corners, and looking to incorporate some cool spot UV layers into the design.

Ive uploaded the existing card front and back as well as our logo.

Card Size Will Be 3.5" x 2"

```html
<!DOCTYPE html>
<html lang="en">
<head>
<meta charset="utf-8">
<title>Fairmont Deck and Rail – Business Card</title>
<link rel="stylesheet" href="https://fonts.googleapis.com/css2?family=Open+Sans:wght@400;600&display=swap">
<style>
  :root {
    --page: #3a3a3c;
    --card: #050505;
    --brand-grey: #c9c9c9;
    --name: #d4d4d4;
    --accent: #1a86cc;
  }
  * { margin: 0; padding: 0; box-sizing: border-box; }
  html, body { width: 1200px; height: 878px; overflow: hidden; }
  body {
    background: var(--page);
    font-family: "Open Sans", Arial, sans-serif;
    position: relative;
  }
  .card {
    position: absolute;
    left: 285px;
    width: 630px;
    height: 360px;
    background: var(--card);
    overflow: hidden;
    box-shadow: 0 10px 30px rgba(0,0,0,.45);
  }
  .card--back { top: 50px; }
  .card--front { top: 460px; }

  .wordmark {
    position: absolute;
    color: var(--brand-grey);
    font-weight: 600;
    letter-spacing: .5px;
    white-space: nowrap;
  }
  .card--back .wordmark {
    left: 0; right: 0; top: 160px;
    text-align: center;
    font-size: 30px;
  }
  .card--front .wordmark {
    left: 48px; top: 150px;
    font-size: 24px;
  }

  .contact-block {
    position: absolute;
    right: 44px;
    top: 70px;
    text-align: right;
  }
  .person-name {
    color: var(--name);
    font-weight: 600;
    font-size: 20px;
    letter-spacing: 1px;
  }
  .person-title {
    color: var(--accent);
    font-size: 15px;
    letter-spacing: 2.5px;
    margin-top: 2px;
  }
  .contact-list {
    list-style: none;
    margin-top: 44px;
    color: var(--accent);
    font-size: 15px;
    line-height: 24px;
  }
  .contact-list li {
    display: flex;
    justify-content: flex-end;
    align-items: center;
    gap: 14px;
  }
  .contact-icon { width: 13px; height: 13px; flex: none; }
  .contact-list .no-icon { padding-right: 27px; }

  .accent-band {
    position: absolute;
    left: 0; right: 0; bottom: 0;
    height: 22px;
    background: var(--accent);
  }
</style>
</head>
<body>
  <section class="card card--back" aria-label="Card back">
    <p class="wordmark">Fairmont Deck and Rail</p>
  </section>

  <section class="card card--front" aria-label="Card front">
    <p class="wordmark">Fairmont Deck and Rail</p>

    <div class="contact-block">
      <p class="person-name">MARCUS ELLERY</p>
      <p class="person-title">PRESIDENT</p>
      <ul class="contact-list">
        <li>403.555.0187
          <svg class="contact-icon" viewBox="0 0 16 16" aria-hidden="true"><path fill="#1a86cc" d="M3 1h3l1.5 4-2 1.3a9 9 0 0 0 4.2 4.2L11 8.5l4 1.5v3a2 2 0 0 1-2 2A12 12 0 0 1 1 3a2 2 0 0 1 2-2z"/></svg>
        </li>
        <li>www.fairmontdeckrail.com
          <svg class="contact-icon" viewBox="0 0 16 16" aria-hidden="true"><g fill="none" stroke="#1a86cc" stroke-width="1.4"><circle cx="8" cy="8" r="6.5"/><ellipse cx="8" cy="8" rx="2.8" ry="6.5"/><path d="M1.5 8h13"/></g></svg>
        </li>
        <li class="no-icon">fairmontdeckrail@mail.com</li>
      </ul>
    </div>

    <div class="accent-band"></div>
  </section>
</body>
</html>
```